Business Card Design for LeafCrest (Farming Devices)

We need Business Cards for our new Company based in Switzerland called "LeafCrest" We develop innovativ products for indoor and outdoor Farming for household and components for vertical farming. Our initial BloomNest gives people the possibility to grow their own food at home all year round. The design should communicate freshness, innovation, health.

```html
<!DOCTYPE html>
<html lang="en">
<head>
<meta charset="utf-8">
<title>LeafCrest Business Card</title>
<link href="https://fonts.googleapis.com/css2?family=Montserrat:wght@400;500;600;700&display=swap" rel="stylesheet">
<style>
  :root {
    --bg: #1b1c1c;
    --green: #6ab43e;
    --green-deep: #3f7d52;
    --teal: #0e3b4b;
    --navy: #06141f;
    --blue: #0a6bbd;
    --ink: #222222;
    --rule: #c4c4c4;
    --white: #ffffff;
  }
  html, body {
    margin: 0;
    padding: 0;
    width: 1200px;
    height: 1200px;
    overflow: hidden;
    background: var(--bg);
    font-family: "Montserrat", sans-serif;
  }
  .sheet {
    width: 1200px;
    height: 1200px;
    display: flex;
    flex-direction: column;
    align-items: center;
    justify-content: center;
    gap: 60px;
  }
  .card {
    position: relative;
    width: 900px;
    height: 514px;
    border-radius: 26px;
    overflow: hidden;
    box-shadow: 0 18px 40px rgba(0,0,0,0.55);
  }
  /* Front */
  .card-front {
    background: linear-gradient(35deg, var(--green) 0%, var(--green-deep) 35%, var(--teal) 68%, var(--navy) 100%);
    display: flex;
    align-items: center;
    justify-content: center;
  }
  .front-name {
    color: var(--white);
    font-weight: 700;
    font-size: 104px;
    letter-spacing: -1px;
  }
  /* Back */
  .card-back {
    background: var(--white);
  }
  .back-name {
    position: absolute;
    right: 110px;
    top: 86px;
    color: var(--green);
    font-weight: 700;
    font-size: 70px;
    letter-spacing: -1px;
  }
  .person {
    position: absolute;
    left: 92px;
    top: 240px;
  }
  .person-name {
    color: var(--blue);
    font-weight: 600;
    font-size: 31px;
    letter-spacing: 0.5px;
    margin: 0;
  }
  .person-role {
    color: var(--ink);
    font-weight: 400;
    font-size: 19px;
    letter-spacing: 1.5px;
    margin: 4px 0 0;
  }
  .rule {
    position: absolute;
    left: 92px;
    right: 60px;
    top: 318px;
    height: 2px;
    background: var(--rule);
  }
  .contacts {
    position: absolute;
    left: 96px;
    top: 338px;
    list-style: none;
    margin: 0;
    padding: 0;
  }
  .contacts li {
    display: flex;
    align-items: center;
    gap: 12px;
    font-size: 20px;
    color: var(--ink);
    line-height: 30px;
  }
  .contacts svg { width: 15px; height: 15px; fill: var(--blue); }
  .address {
    position: absolute;
    right: 60px;
    top: 336px;
    text-align: right;
    font-size: 18px;
    line-height: 24px;
    color: var(--ink);
  }
  .band-green {
    position: absolute;
    left: 0;
    bottom: 30px;
    width: 650px;
    height: 5px;
    background: var(--green);
  }
  .band-blue {
    position: absolute;
    left: 0;
    right: 0;
    bottom: 0;
    height: 24px;
    background: var(--blue);
  }
  .web-block {
    position: absolute;
    left: 650px;
    right: 0;
    bottom: 0;
    height: 86px;
    background: var(--blue);
    color: var(--white);
    font-size: 20px;
    display: flex;
    align-items: center;
    justify-content: flex-end;
    padding-right: 40px;
  }
  .web-block b { font-weight: 700; }
</style>
</head>
<body>
<main class="sheet">
  <section class="card card-front">
    <div class="front-name">LeafCrest</div>
  </section>

  <section class="card card-back">
    <div class="back-name">LeafCrest</div>

    <div class="person">
      <p class="person-name">LUKAS MEIER</p>
      <p class="person-role">DIRECTOR</p>
    </div>

    <div class="rule"></div>

    <ul class="contacts">
      <li>
        <svg viewBox="0 0 24 24" aria-hidden="true"><path d="M6.6 10.8a15.1 15.1 0 0 0 6.6 6.6l2.2-2.2c.3-.3.7-.4 1-.2 1.1.4 2.3.6 3.6.6.6 0 1 .4 1 1V20c0 .6-.4 1-1 1A17 17 0 0 1 3 4c0-.6.4-1 1-1h3.5c.6 0 1 .4 1 1 0 1.3.2 2.5.6 3.6.1.3 0 .7-.2 1z"/></svg>
        +41 4 5127 3360
      </li>
      <li>
        <svg viewBox="0 0 24 24" aria-hidden="true"><path d="M2 5h20v14H2z M4 7v.5l8 5 8-5V7z" fill-rule="evenodd"/></svg>
        hello@leafcrest.ch
      </li>
    </ul>

    <div class="address">14/27 Linden Strasse<br>Zug 6300, Switzerland</div>

    <div class="band-green"></div>
    <div class="band-blue"></div>
    <div class="web-block">www.<b>leafcrest</b>.ch</div>
  </section>
</main>
</body>
</html>
```